New logo and common packaging design theme

We are a modern tea company selling teas from around the World. We need a innovative packaging artwork ( A label design that is 11.5 inches wide and 5 inches in height)that can be used across all of our products as well as a new logo that goes with this artwork. Details of the current logo and color schemes are available on our website at www.7koru7.com. The intend is not to change the entire website's color scheme because of the new artwork and logo, but come up with something that matches or complements the color theme of the current website, but with a new modern and clean logo and packaging artwork theme that can be carried through the products.

Target Market(s)

sophisticated audience who seek a modern lifestyle, city dwellers

Industry/Entity Type

It Company

Requirements
Must have
• Modern, clean look and feel

```html
<!DOCTYPE html>
<html lang="en">
<head>
<meta charset="utf-8">
<title>Raspberry Green Tea Label</title>
<link rel="stylesheet" href="https://fonts.googleapis.com/css2?family=Comfortaa:wght@700&family=Noto+Sans:wght@400;700&display=swap">
<style>
  :root {
    --paper: #ffffff;
    --frame-orange: #e8a21a;
    --band-grey: #6b7781;
    --fold-navy: #263446;
    --ink: #111111;
    --title-ink: #ffffff;
    --bowl-rim: #f4f1ee;
    --leaf-red: #9c2a2e;
    --leaf-dark: #4a2a22;
    --brand-ink: #1b1b1b;
    --brand-dot: #e8a21a;
  }
  html, body {
    margin: 0;
    padding: 0;
    width: 1200px;
    height: 522px;
    overflow: hidden;
    background: var(--paper);
  }
  .label {
    display: block;
    width: 1200px;
    height: 522px;
  }
  .label-frame { fill: none; stroke: var(--frame-orange); stroke-width: 6; }
  .title-band { fill: var(--band-grey); }
  .band-fold { fill: var(--fold-navy); }
  .product-title {
    font-family: "Comfortaa", sans-serif;
    font-weight: 700;
    font-size: 64px;
    fill: var(--title-ink);
    letter-spacing: 1px;
  }
  .copy {
    font-family: "Noto Sans", sans-serif;
    font-weight: 400;
    font-size: 21.5px;
    fill: var(--ink);
  }
  .bowl-rim { fill: var(--bowl-rim); stroke: #d9d4cf; stroke-width: 2; }
  .brand-name {
    font-family: "Noto Sans", sans-serif;
    font-weight: 700;
    font-size: 66px;
    fill: var(--brand-ink);
  }
  .brand-dot { fill: var(--brand-dot); }
</style>
</head>
<body>
<svg class="label" viewBox="0 0 1200 522" xmlns="http://www.w3.org/2000/svg">
  <defs>
    <radialGradient id="tea-leaves" cx="50%" cy="50%" r="50%">
      <stop offset="0%" stop-color="var(--leaf-red)"/>
      <stop offset="70%" stop-color="#7a3a2c"/>
      <stop offset="100%" stop-color="var(--leaf-dark)"/>
    </radialGradient>
  </defs>

  <rect class="label-frame" x="32" y="28" width="1136" height="466"/>

  <polygon class="band-fold" points="0,65 32,44 32,65"/>
  <polygon class="band-fold" points="1200,65 1168,44 1168,65"/>
  <rect class="title-band" x="0" y="65" width="1200" height="84"/>
  <text class="product-title" x="630" y="126" text-anchor="middle">raspberry green tea</text>

  <text class="copy" x="48" y="212">Raspberry Green tea is a perfect blend of green tea and natural vine ripened Oregon</text>
  <text class="copy" x="48" y="240">raspberry with natural flavors.</text>
  <text class="copy" x="222" y="270">Green tea is a rich source of antioxidants, natural substances found in</text>
  <text class="copy" x="285" y="299">and vegetables, which form an important part of a healthy diet.</text>
  <text class="copy" x="335" y="331">Product Quantity : 1/4 lb</text>
  <text class="copy" x="335" y="361">Approximately makes 50 cups of tea</text>

  <g class="product-bowl" role="img" aria-label="White bowl of loose raspberry green tea leaves">
    <circle class="bowl-rim" cx="130" cy="418" r="152"/>
    <circle cx="130" cy="418" r="128" fill="url(#tea-leaves)"/>
  </g>

  <g class="brand">
    <circle class="brand-dot" cx="650" cy="432" r="44"/>
    <text class="brand-name" x="720" y="456">7koru7.com</text>
  </g>
</svg>
</body>
</html>
```